Quite your look: needs a logo design and a business card

The business name is called: Quite your look. It's all about fashion for everyone who needs to gain confidence and find his own style: Image Consultant, Personal Shopper. Here my Facebook fan page: https://www.examplebook.test/pages/Quite-your-look/804213967520431

I would like a smart logo & business card. The design has to be smart and long lasting. I like simplicity ("less is more"). The image needs to bring over seriousness and style. I target people from 35-65 years old. I would love to have smart warm colours like brown mole or anthracite, eventually with some berry or bordeaux red.

The copy is the following:
Quite your look
Daphne Volkers
Mobile: +27 71 436 02 59
eMail: volkers.daphne@mailbox.test
Cape Town

Target Market(s)

Core target group: 35-65 years old women; wealthy; living in Cape Town
Larger target group: South Africa; eventually men too

Industry/Entity Type

Business

```html
<!DOCTYPE html>
<html lang="en">
<head>
<meta charset="utf-8">
<title>Quite your look – Business Card</title>
<link rel="stylesheet" href="https://fonts.googleapis.com/css2?family=Arimo:wght@400&display=swap">
<style>
  :root {
    --canvas: #ffffff;
    --card: #e6e7e7;
    --band: #6d6e71;
    --ink: #111111;
    --mark: #0d0d0d;
    --faint-mark: #a7a9ac;
    --faint-name: #8a8c8f;
    --light-text: #ffffff;
  }
  html, body {
    margin: 0;
    padding: 0;
    width: 1200px;
    height: 1000px;
    overflow: hidden;
    background: var(--canvas);
  }
  .canvas {
    position: relative;
    width: 1200px;
    height: 1000px;
    font-family: "Arimo", Arial, sans-serif;
  }
  .card {
    position: absolute;
    top: 327px;
    width: 461px;
    height: 289px;
    background: var(--card);
    overflow: hidden;
  }
  .card--front { left: 122px; }
  .card--back { left: 632px; }
  .card__band {
    position: absolute;
    inset: 0;
  }
  .brand-dot {
    position: absolute;
    left: 23px;
    top: 20px;
    width: 112px;
    height: 100px;
    border-radius: 50%;
    background: var(--mark);
  }
  .brand-name {
    position: absolute;
    left: 148px;
    top: 44px;
    margin: 0;
    font-size: 38px;
    font-weight: 400;
    color: var(--ink);
    white-space: nowrap;
  }
  .contact {
    position: absolute;
    left: 186px;
    top: 134px;
    font-size: 19px;
    line-height: 25px;
    color: var(--ink);
  }
  .contact p, .details p { margin: 0; }
  .details {
    position: absolute;
    left: 23px;
    top: 245px;
    font-size: 13px;
    line-height: 17px;
    color: var(--light-text);
  }
  .back-dot {
    position: absolute;
    left: 95px;
    top: 16px;
    width: 244px;
    height: 220px;
    border-radius: 50%;
    background: var(--faint-mark);
  }
  .back-name {
    position: absolute;
    left: 70px;
    top: 214px;
    margin: 0;
    font-size: 46px;
    font-weight: 400;
    color: var(--faint-name);
    white-space: nowrap;
  }
</style>
</head>
<body>
<main class="canvas">
  <section class="card card--front" aria-label="Business card front">
    <svg class="card__band" width="461" height="289" viewBox="0 0 461 289" aria-hidden="true">
      <path d="M0,81 C20,160 200,215 461,289 L0,289 Z" fill="var(--band)"/>
    </svg>
    <div class="brand-dot" aria-hidden="true"></div>
    <h1 class="brand-name">Quite your look</h1>
    <div class="contact">
      <p>Daphne Volkers</p>
      <p>Mobile: +27 71 436 02 59</p>
    </div>
    <div class="details">
      <p>eMail: volkers.daphne@mailbox.test</p>
      <p>Cape Town</p>
    </div>
  </section>

  <section class="card card--back" aria-label="Business card back">
    <div class="back-dot" aria-hidden="true"></div>
    <p class="back-name">Quite your look</p>
  </section>
</main>
</body>
</html>
```